Website Design

I require a website to be built around a CMS for a commercial client, an SME in the construction industry
I am happy to approach this 2 ways - either a full site redesign and build around a well known CMS by the successful candidate. Or a page template designed which I can then duplicate and use with a light CMS - I have enough coding experience to implement this myself.
I require a html/css file as the final piece of work,
Updates
Hi,
This is the site to be redesigned:
http://www.verntowers.co.uk/
As you can see it is quite dated.
The design should be quite focused on the images and photos of the products.
2 designs which were reject can be seen here:
verntowers.quillpixel.co.uk
verntowers2.quillpixel.co.uk
This is the clients main competitor: http://www.pelicanreach.com/ - They are keen to have a site which is 'better' than this one.
Hope this info helps. The site will include a lightbox gallery to focus on products, please bare this is mind when submitting your designs.
Reason: Need a higher number of designs to take to the client.
We are happy just to accept PSD designs if you believe the budget is too low for a HTML design. Please get in touch if you require more info.
Please can you use the customers logo from the website in designs. Thanks
Reason: Need more designers!
Target Market(s)
Industrial/Construction Sector
Industry/Entity Type
Construction
Requirements
Must have
- final design must be in html

```html
<!DOCTYPE html>
<html lang="en">
<head>
<meta charset="utf-8">
<title>Vern Towers Ltd.</title>
<link rel="stylesheet" href="https://fonts.googleapis.com/css2?family=Fira+Sans:wght@400;500;600&family=Noto+Sans:wght@400;700&family=Yanone+Kaffeesatz:wght@400;500&display=swap">
<style>
:root{
  --navy:#34415f;
  --navy-dark:#2a3550;
  --orange:#f5a800;
  --page:#ebebeb;
  --side:#6f8fc4;
  --text:#1b1b1b;
  --link:#1a3fd6;
  --white:#ffffff;
  --border:#cfcfcf;
}
html,body{margin:0;padding:0;overflow:hidden;background:var(--page);}
.canvas{position:relative;width:1200px;height:1191px;overflow:hidden;background:var(--page);font-family:"Noto Sans",sans-serif;color:var(--text);}
.side-band{position:absolute;top:0;width:25px;height:1191px;background:var(--side);}
.side-band.left{left:0;}
.side-band.right{right:0;width:31px;}

/* header */
.header{position:absolute;left:37px;top:0;width:1119px;height:240px;background:var(--navy);box-shadow:0 1px 3px rgba(0,0,0,.3);}
.brand-box{position:absolute;left:25px;top:21px;width:273px;height:125px;background:var(--white);display:flex;align-items:center;justify-content:center;gap:10px;}
.brand-box .mark{width:16px;height:16px;background:var(--navy);}
.brand-box .name{font-family:"Fira Sans",sans-serif;font-weight:600;font-size:30px;color:var(--navy);letter-spacing:1px;}
.brand-fold{position:absolute;left:25px;top:146px;width:0;height:0;border-top:10px solid #1c2438;border-left:14px solid transparent;}
.company{position:absolute;left:56px;top:150px;font-family:"Yanone Kaffeesatz",sans-serif;font-weight:500;font-size:36px;color:var(--orange);letter-spacing:.5px;line-height:1;}
.phone{position:absolute;left:58px;top:192px;display:flex;align-items:center;gap:10px;}
.phone-number{font-family:"Fira Sans",sans-serif;font-size:26px;color:var(--white);}
.tagline{position:absolute;left:667px;top:24px;font-family:"Fira Sans",sans-serif;font-size:26px;line-height:34px;color:var(--white);}
.search{position:absolute;left:894px;top:185px;display:flex;}
.search-input{width:212px;height:25px;background:var(--white);font-size:12px;color:#9a9a9a;line-height:25px;padding-left:8px;box-sizing:border-box;}
.search-button{width:29px;height:25px;background:var(--orange);display:flex;align-items:center;justify-content:center;}

/* showcase */
.showcase{position:absolute;left:37px;top:258px;width:1119px;height:323px;box-sizing:border-box;border:1px solid var(--border);background:linear-gradient(#f7f7f7 0%,#f4f4f4 40%,#dcdcdc 48%,#f3f3f3 100%);}
.floor{position:absolute;left:49px;top:513px;width:1099px;height:66px;background:linear-gradient(rgba(200,200,205,.55),rgba(240,240,240,0));}
.tab-photo{position:absolute;}
.tab-spine{position:absolute;width:47px;background:var(--navy);box-shadow:2px 0 3px rgba(0,0,0,.25);}
.tab-spine span{position:absolute;left:7px;top:10px;writing-mode:vertical-rl;font-family:"Yanone Kaffeesatz",sans-serif;font-size:31px;color:var(--white);line-height:1;}
.tab-spine.active span{color:var(--orange);}

/* welcome */
.welcome{position:absolute;left:37px;top:598px;width:457px;height:424px;background:linear-gradient(90deg,#e4e4e4,#f0f0f0 6%,#f0f0f0 94%,#e4e4e4);}
.welcome h1{position:absolute;left:19px;top:2px;margin:0;font-family:"Fira Sans",sans-serif;font-weight:500;font-size:27px;color:var(--navy);}
.welcome .body{position:absolute;left:21px;top:46px;width:418px;font-size:13.4px;line-height:20.1px;}
.welcome p{margin:0 0 20px;}
.welcome .rule{position:absolute;left:19px;top:385px;width:419px;height:1px;background:var(--navy);}
.welcome .more{position:absolute;right:19px;top:393px;font-size:14px;color:var(--link);text-decoration:underline;}

/* panels */
.panel{position:absolute;top:604px;height:381px;background:var(--navy);box-shadow:0 1px 3px rgba(0,0,0,.35);color:var(--white);}
.panel.news{left:512px;width:317px;}
.panel.projects{left:839px;width:317px;}
.panel h2{position:absolute;left:12px;top:6px;margin:0;font-family:"Fira Sans",sans-serif;font-weight:600;font-size:27px;}
.panel h2 em{font-style:normal;color:var(--orange);}
.news-title{position:absolute;left:12px;font-size:12.4px;font-weight:700;}
.news-sub{position:absolute;left:12px;font-size:12.4px;font-weight:700;color:var(--orange);}
.photo-frame{position:absolute;left:12px;width:294px;box-sizing:border-box;border:1px solid var(--white);}
.project{position:absolute;left:15px;width:290px;height:115px;}
.project .thumb{position:absolute;left:0;top:0;width:90px;height:89px;border:1px solid var(--white);box-sizing:border-box;background:linear-gradient(135deg,#7f8fb3,#c9b9a8 55%,#8a5a4a);}
.project .title{position:absolute;left:103px;top:0;font-size:12.4px;font-weight:700;}
.project .date{position:absolute;left:103px;top:18px;font-size:12.4px;font-weight:700;color:var(--orange);}
.project .summary{position:absolute;left:103px;top:36px;width:185px;font-size:11.6px;line-height:16px;}
.project .read{position:absolute;right:0;top:92px;font-size:12px;color:var(--orange);display:flex;align-items:center;gap:6px;}
.panel-rule{position:absolute;left:0;top:332px;width:317px;height:1px;background:#4d5a78;}
.view-all{position:absolute;right:24px;top:345px;font-family:"Fira Sans",sans-serif;font-weight:500;font-size:20px;}
.view-all em{font-style:normal;color:var(--orange);}

/* nav + footer */
.nav{position:absolute;left:37px;top:1050px;width:1119px;height:34px;background:var(--navy);display:flex;justify-content:space-between;align-items:center;padding:0 18px;box-sizing:border-box;font-size:12.4px;font-weight:700;color:var(--white);}
.footer{position:absolute;left:37px;top:1089px;width:1119px;height:75px;box-sizing:border-box;border:1px solid #d6d6d6;background:linear-gradient(#d9d9d9,#f3f3f3 40%,#e2e2e2);padding:11px 13px;font-size:11.6px;line-height:15.6px;color:#111;}
.footer b{font-weight:700;}
</style>
</head>
<body>
<div class="canvas">
  <div class="side-band left" role="img" aria-label="Blue diagonal stripe border"></div>
  <div class="side-band right" role="img" aria-label="Blue diagonal stripe border"></div>

  <header class="header">
    <div class="brand-box"><span class="mark"></span><span class="name">VERN TOWERS</span></div>
    <div class="company">VERN TOWERS LTD.</div>
    <div class="phone">
      <svg width="29" height="36" viewBox="0 0 29 36" aria-hidden="true"><path d="M6 3c2-1 4 0 5 2l2 5c1 2 0 3-2 4l-1 1c1 4 3 7 6 10l2-1c2-1 3-1 4 1l3 4c1 2 0 3-2 4-3 2-7 2-10-1C7 26 3 18 3 10c0-3 1-6 3-7z" fill="#d8262b"/><rect x="2" y="33" width="25" height="2" fill="#7d8597"/></svg>
      <span class="phone-number">01632 960 418</span>
    </div>
    <div class="tagline">We Design &amp; Manufacture Solutions for<br>Difficult Access Problems.</div>
    <div class="search">
      <div class="search-input">Search...</div>
      <div class="search-button"><svg width="18" height="18" viewBox="0 0 18 18" aria-hidden="true"><circle cx="10.5" cy="7.5" r="5" fill="none" stroke="#111" stroke-width="2"/><path d="M7 11l-5 5" stroke="#111" stroke-width="3" stroke-linecap="round"/></svg></div>
    </div>
  </header>
  <div class="brand-fold"></div>

  <section class="showcase"></section>
  <div class="floor"></div>

  <div class="tab-photo" style="left:49px;top:279px;width:242px;height:234px;background:linear-gradient(160deg,#5d6a78,#2f3a44 60%,#8a8f92);" role="img" aria-label="Workers on a suspended access cradle"></div>
  <div class="tab-spine active" style="left:290px;top:279px;height:234px;"><span>HOME</span></div>

  <div class="tab-photo" style="left:337px;top:285px;width:126px;height:220px;background:linear-gradient(170deg,#6b6560,#8a8a7a 50%,#5f7a63);" role="img" aria-label="Engineers working on site"></div>
  <div class="tab-spine" style="left:462px;top:285px;height:220px;"><span>Services</span></div>

  <div class="tab-photo" style="left:509px;top:293px;width:110px;height:200px;background:linear-gradient(#f2d2b4,#8ec6ea 50%,#f2d2b4);" role="img" aria-label="Technical drawing of a hoist mechanism"></div>
  <div class="tab-spine" style="left:619px;top:293px;height:200px;"><span>Hoists</span></div>

  <div class="tab-photo" style="left:666px;top:299px;width:94px;height:187px;background:linear-gradient(#9fb6d6,#a0664a 40%,#8a8076);" role="img" aria-label="Building under construction with scaffolding"></div>
  <div class="tab-spine" style="left:760px;top:299px;height:187px;"><span>Example</span></div>

  <div class="tab-photo" style="left:807px;top:305px;width:89px;height:173px;background:linear-gradient(150deg,#d9d9d9,#b0b4b8 45%,#2c55a0);" role="img" aria-label="Fall arrest harness clips"></div>
  <div class="tab-spine" style="left:896px;top:305px;height:173px;"><span>FallAresque</span></div>

  <div class="tab-photo" style="left:943px;top:313px;width:68px;height:157px;background:linear-gradient(#b9c7c7,#6f8585);" role="img" aria-label="Mast climbing platform"></div>
  <div class="tab-spine" style="left:1011px;top:313px;height:157px;"><span>Mast Climber</span></div>

  <div class="tab-photo" style="left:1058px;top:317px;width:43px;height:146px;background:linear-gradient(#8aa0bf,#cfd8e4 50%,#5c7396);" role="img" aria-label="Email symbol graphic"></div>
  <div class="tab-spine" style="left:1100px;top:317px;height:146px;"><span>Contact Us</span></div>

  <section class="welcome">
    <h1>Welcome</h1>
    <div class="body">
      <p>Lorem ipsum dolor sit amet, consectetur adipiscing elit. Nulla vehicula convallis mauris eget vulputate. Quisque ac augue nunc, vel malesuada mauris. Etiam vel enim massa. Mauris feugiat nisi a dui pretium egestas. Nulla facilisi. Etiam non sollicitudin sem. Ut iaculis risus in mi dignissim sit amet mollis tellus imperdiet. Curabitur vel tortor ac magna hendrerit pellentesque ac euismod neque. Maecenas quis erat vel dolor egestas varius.</p>
      <p>Lorem ipsum dolor sit amet, consectetur adipiscing elit. Nulla vehicula convallis mauris eget vulputate. Quisque ac augue nunc, vel malesuada mauris. Etiam vel enim massa. Mauris feugiat nisi a dui pretium egestas. Nulla facilisi. Etiam non sollicitudin sem. Ut iaculis risus in mi dignissim sit amet mollis tellus imperdiet. Curabitur vel tortor ac magna hendrerit</p>
    </div>
    <div class="rule"></div>
    <div class="more">More About Vern Towers LTD.</div>
  </section>

  <section class="panel news">
    <h2>Latest <em>News</em></h2>
    <div class="news-title" style="top:63px;">The NEW 1500 mm X-beam</div>
    <div class="news-sub" style="top:81px;">As seen at the Halden Expo</div>
    <div class="photo-frame" style="top:98px;height:105px;background:linear-gradient(#a9b4b8,#b5a98a 40%,#9a9a8a);" role="img" aria-label="New aluminium beam laid out in a yard"></div>
    <div class="news-title" style="top:251px;">Visit our Tanks Website</div>
    <div class="photo-frame" style="top:269px;height:79px;background:linear-gradient(#5a8fd0,#9db6c8 45%,#6d7a80);" role="img" aria-label="Large steel storage tank against blue sky"></div>
  </section>

  <section class="panel projects">
    <h2>Latest <em>Projects</em></h2>
    <div class="project" style="top:56px;">
      <div class="thumb" role="img" aria-label="Access gantry on a building facade"></div>
      <div class="title">Lorem Ipsum</div>
      <div class="date">17th Dec, 2011</div>
      <div class="summary">Lorem ipsum dolor sit amet, consectetur adipiscing elit. Nulla vehicula convallis mauris eget</div>
      <div class="read"><svg width="9" height="9" viewBox="0 0 9 9" aria-hidden="true"><path d="M0 0l4 4.5L0 9zM4 0l4 4.5L4 9z" fill="#f5a800"/></svg>Read More</div>
    </div>
    <div class="project" style="top:207px;">
      <div class="thumb" role="img" aria-label="Access gantry on a building facade"></div>
      <div class="title">Lorem Ipsum</div>
      <div class="date">17th Dec, 2011</div>
      <div class="summary">Lorem ipsum dolor sit amet, consectetur adipiscing elit. Nulla vehicula convallis mauris eget</div>
      <div class="read"><svg width="9" height="9" viewBox="0 0 9 9" aria-hidden="true"><path d="M0 0l4 4.5L0 9zM4 0l4 4.5L4 9z" fill="#f5a800"/></svg>Read More</div>
    </div>
    <div class="panel-rule"></div>
    <div class="view-all">View All <em>Latest Projects</em></div>
  </section>

  <nav class="nav">
    <span>Home</span><span>|</span><span>About Us</span><span>|</span><span>Services</span><span>|</span><span>Hoists</span><span>|</span><span>Fall Aresque</span><span>|</span><span>Mast Climber</span><span>|</span><span>Contact Us</span><span>|</span><span>Sitemap</span>
  </nav>

  <footer class="footer">
    <b>Vern Towers LTD.</b><br>
    <b>Registered Office:</b> 17 Ridgeway Lane, Hoyle, Kelmsfield, West Riding, KF4 2RT. Tel: (01632) 960418 | Fax: (01632) 960733 | Email: info@verntowers.co.uk<br>
    © 2011, All Rights Reserved
  </footer>
</div>
</body>
</html>
```